We need a flyer where we promote a workshop to our members of the jewish community www.qvb-gemeinde.example . The workshop is calles "guidance in ten seasons presented by QVB. We would like to see a flyer with the below text is used and also some pictures (attached). The flyer should come over as cool, fresh, innovative for a younger crowd so called young professionals (age 28-35).
TITLE.
"Guidance in Ten Seasons.
SUBTITLE.
Your systematic self-coaching roadmap to power and impact—and your future.”
TEXT.
Dr. Martin K. Halvorsen is the CEO Emeritus of Alpine Advisory Partners—he made an exit in 2013. He is the award-winning author of 8 books, including "Plan-Into-Motion," "Speak or Falter" and "The Cantor and the Chairman.”
For the past 20 years he has taught leadership at Harwick University in New York and at BKU (Lindenberg University) to prepare future CEOs and other leaders in business, government , nonprofits and the military.
Now, in a process exclusively designed for QVB’s next generation of emerging leaders, Martin unpacks his leadership secrets in 3 action-packed labs—reduced to the max:
Lab 1. Guidance in Ten Seasons: The Summit Guide Triangle®. Self-Assessment. Self-Leadership: “The Lantern.” 5-Year Vision. 100-Day Catalytic Project.
Lab 2. Leading Through Language. Relationship: Building Trust. Plan-Into-Motion. Cockpit.
Lab 3. Debrief and Scale-Up. Sustainability. Action Tools.
Do you want to build your own future and a life you love? Do you want to jump-start that future and life over 100 days while learning a toolbox of leadership skills, networking with like-minded people—and even get some pizza? Then join us.
Target Market(s)
young professionals age 28-35

```html
<!DOCTYPE html>
<html lang="en">
<head>
<meta charset="utf-8">
<title>QVB Presents – Guidance in Ten Seasons</title>
<link href="https://fonts.googleapis.com/css2?family=Montserrat:wght@800&family=Open+Sans:wght@700&family=Carlito:wght@400;700&display=swap" rel="stylesheet">
<style>
  :root {
    --red: #e14a4c;
    --red-deep: #e04b4d;
    --blue: #1a86d4;
    --blue-light: #3aa0e6;
    --ink: #1d1d1f;
    --white: #ffffff;
    --lab-1: #5fc4b0;
    --lab-2: #8ed3c4;
    --lab-3: #b4e3d9;
    --backdrop: #e9e9e9;
  }
  * { box-sizing: border-box; margin: 0; padding: 0; }
  html, body { width: 1200px; height: 1000px; overflow: hidden; background: var(--backdrop); }
  .canvas { position: relative; width: 1200px; height: 1000px; }
  .flyer {
    position: absolute; left: 235px; top: 30px; width: 730px; height: 940px;
    background: var(--white); overflow: hidden;
    font-family: "Carlito", Calibri, Arial, sans-serif; color: var(--ink);
    box-shadow: 0 4px 16px rgba(0,0,0,.18);
  }
  .presents-band {
    position: absolute; left: 0; top: 0; width: 100%; height: 70px; background: var(--red);
  }
  .presents {
    position: absolute; left: 152px; top: 20px;
    font-family: "Open Sans", Arial, sans-serif; font-weight: 700; font-size: 30px; color: var(--white);
  }
  .title-band {
    position: absolute; left: 0; top: 70px; width: 100%; height: 165px;
    background: linear-gradient(90deg, var(--blue) 0%, var(--blue-light) 55%, var(--blue) 100%);
  }
  .title {
    position: absolute; left: 36px; top: 84px; width: 460px;
    font-family: "Montserrat", Arial, sans-serif; font-weight: 800; font-size: 41px; line-height: 72px;
    color: var(--white); text-transform: uppercase; white-space: nowrap;
  }
  .speaker-photo {
    position: absolute; left: 505px; top: 15px; width: 215px; height: 307px;
    background: linear-gradient(180deg, #c9a59a 0%, #8c6f68 35%, #5b5f66 70%, #4a4e55 100%);
  }
  .subtitle {
    position: absolute; left: 30px; top: 258px; width: 450px;
    font-family: "Open Sans", Arial, sans-serif;
    font-weight: 700; font-size: 18.5px; line-height: 23px; text-align: center;
  }
  .bio {
    position: absolute; left: 35px; top: 332px; width: 652px;
    font-size: 17px; line-height: 22px;
  }
  .bio p { margin-bottom: 12px; text-align: justify; }
  .labs { position: absolute; left: 35px; top: 543px; width: 650px; }
  .lab { display: flex; margin-bottom: 10px; font-size: 16.5px; line-height: 21px; }
  .lab-label { width: 66px; display: flex; align-items: center; justify-content: center; }
  .lab-text { flex: 1; margin-left: 8px; padding: 5px 10px; display: flex; align-items: center; text-align: justify; }
  .lab--1 .lab-label, .lab--1 .lab-text { background: var(--lab-1); min-height: 57px; }
  .lab--2 .lab-label, .lab--2 .lab-text { background: var(--lab-2); min-height: 56px; }
  .lab--3 .lab-label, .lab--3 .lab-text { background: var(--lab-3); min-height: 35px; }
  .question {
    position: absolute; left: 50px; top: 724px;
    font-family: "Open Sans", Arial, sans-serif; font-weight: 700; font-size: 13px;
  }
  .cta-box {
    position: absolute; left: 35px; top: 750px; width: 650px; height: 82px;
    border: 2px solid var(--red);
  }
  .cta-text {
    position: absolute; left: 12px; top: 10px; width: 410px;
    font-family: "Open Sans", Arial, sans-serif;
    font-weight: 700; font-size: 13px; line-height: 19px; text-align: justify;
  }
  .cta-text .pizza { font-size: 16px; }
  .cta-join {
    position: absolute; right: 3px; top: 4px; width: 196px; height: 71px; background: var(--red);
    color: var(--white); text-align: center; font-family: "Open Sans", Arial, sans-serif; font-weight: 700;
  }
  .cta-join .join { font-size: 26px; line-height: 34px; margin-top: 6px; }
  .cta-join .date { font-size: 19px; line-height: 22px; }
  .footer-band {
    position: absolute; left: 0; bottom: 0; width: 100%; height: 97px; background: var(--red-deep);
    display: flex; align-items: center; justify-content: center;
    font-size: 22px; color: var(--ink);
  }
</style>
</head>
<body>
<div class="canvas">
  <article class="flyer">
    <div class="presents-band"></div>
    <div class="title-band"></div>
    <div class="presents">QVB Presents</div>
    <h1 class="title">Guidance<br>in Ten Seasons</h1>
    <div class="speaker-photo" role="img" aria-label="Portrait photo of the speaker, arms crossed, in a grey blazer"></div>

    <p class="subtitle">Your systematic self-coaching roadmap<br>to power and impact—and your future.”</p>

    <div class="bio">
      <p>Dr. Martin K. Halvorsen is the CEO Emeritus of Alpine Advisory Partners—he made an exit in 2013. He is the award-winning author of 8 books, including "Plan-Into-Motion," "Speak or Falter" and "The Cantor and the Chairman.”</p>
      <p>For the past 20 years he has taught leadership at Harwick University in New York and at BKU (Lindenberg University) to prepare future CEOs and other leaders in business, government , nonprofits and the military.</p>
      <p>Now, in a process exclusively designed for QVB’s next generation of emerging leaders, Martin unpacks his leadership secrets in 3 action-packed labs—reduced to the max:</p>
    </div>

    <div class="labs">
      <div class="lab lab--1">
        <div class="lab-label">Lab 1.</div>
        <div class="lab-text">Guidance in Ten Seasons: The Summit Guide Triangle®. Self-Assessment. Self-Leadership: “The Lantern.” 5-Year Vision. 100-Day Catalytic Project.</div>
      </div>
      <div class="lab lab--2">
        <div class="lab-label">Lab 2.</div>
        <div class="lab-text">Leading Through Language. Relationship: Building Trust. Plan-Into-Motion. Cockpit.</div>
      </div>
      <div class="lab lab--3">
        <div class="lab-label">Lab 3.</div>
        <div class="lab-text">Debrief and Scale-Up. Sustainability. Action Tools.</div>
      </div>
    </div>

    <p class="question">Do you want to build your own future and a life you love?</p>

    <div class="cta-box">
      <p class="cta-text">Do you want to jump-start that future and life over 100 days while learning a toolbox of leadership skills, networking with like-minded people - <span class="pizza">and even get some pizza?</span></p>
      <div class="cta-join">
        <div class="join">Then join us</div>
        <div class="date">Date : TBA</div>
      </div>
    </div>

    <footer class="footer-band">Address information | Contact information</footer>
  </article>
</div>
</body>
</html>
```